New Business Card Design Project

Want a simple but attention grabbing business card. Back Side having mainly our logo and basic info-the front side a typical business card.

Contact Information for Business Card

Hearth & Basin Works
218 NW Larkfield Rd. Suite 207
Ankeny, Iowa 50021

phone- 515.284.7093

website is -hbwplains.com

```html
<!DOCTYPE html>
<html lang="en">
<head>
<meta charset="utf-8">
<title>Hearth &amp; Basin Works – Business Cards</title>
<link rel="stylesheet" href="https://fonts.googleapis.com/css2?family=Montserrat:wght@600;700;800&family=Open+Sans:wght@400;600&display=swap">
<style>
  :root {
    --backdrop: #1e1e20;
    --navy: #0c1424;
    --orange: #ee5c26;
    --blue: #2372c2;
    --white: #ffffff;
    --card-w: 560px;
    --card-h: 320px;
  }
  * { box-sizing: border-box; margin: 0; padding: 0; }
  html, body {
    width: 1200px; height: 780px; overflow: hidden;
    background: var(--backdrop);
  }
  .canvas { position: relative; width: 1200px; height: 780px; }
  .card {
    position: absolute;
    width: var(--card-w); height: var(--card-h);
    border-radius: 22px; overflow: hidden;
    background: var(--navy);
    box-shadow: 0 18px 40px rgba(0,0,0,.55);
  }
  .card-logo-side { left: 70px; top: 60px; }
  .card-info-side { left: 570px; top: 400px; }
  .card-shapes { position: absolute; inset: 0; width: 100%; height: 100%; }

  .brand-name {
    position: absolute;
    font-family: "Montserrat", sans-serif;
    font-weight: 700;
    color: var(--orange);
    text-transform: uppercase;
    white-space: nowrap;
    display: flex; align-items: center; gap: 10px;
  }
  .brand-mark { display: inline-block; background: var(--orange); }
  .card-logo-side .brand-name { right: 44px; top: 180px; font-size: 22px; letter-spacing: .5px; }
  .card-logo-side .brand-mark { width: 13px; height: 13px; }
  .card-info-side .brand-name { left: 28px; top: 40px; font-size: 13px; letter-spacing: .5px; gap: 7px; }
  .card-info-side .brand-mark { width: 9px; height: 9px; }

  .contact-list {
    position: absolute; left: 320px; top: 116px;
    list-style: none;
    font-family: "Open Sans", sans-serif;
    font-size: 12px; line-height: 1.3;
    color: var(--white);
  }
  .contact-item { display: flex; align-items: flex-start; gap: 9px; margin-bottom: 11px; }
  .contact-icon { width: 13px; height: 13px; flex: none; margin-top: 1px; fill: var(--orange); }

  .person { position: absolute; left: 150px; bottom: 40px; }
  .person-name {
    font-family: "Montserrat", sans-serif; font-weight: 800;
    font-size: 22px; text-transform: uppercase; letter-spacing: .3px;
    white-space: nowrap;
  }
  .person-name .first { color: var(--blue); }
  .person-name .last { color: var(--orange); }
  .person-title {
    margin-top: 4px;
    font-family: "Open Sans", sans-serif; font-weight: 600;
    font-size: 10px; letter-spacing: 4px; color: var(--white);
  }
</style>
</head>
<body>
<main class="canvas">

  <section class="card card-logo-side">
    <svg class="card-shapes" viewBox="0 0 560 320" aria-hidden="true">
      <polygon points="0,0 560,0 560,66 232,98 0,252" fill="var(--orange)"/>
      <polygon points="0,252 232,98 560,66 560,82 252,118 0,272" fill="var(--blue)"/>
    </svg>
    <div class="brand-name"><span class="brand-mark"></span>Hearth &amp; Basin Works</div>
  </section>

  <section class="card card-info-side">
    <svg class="card-shapes" viewBox="0 0 560 320" aria-hidden="true">
      <polygon points="0,296 292,76 560,50 560,66 316,100 0,326" fill="var(--blue)"/>
    </svg>

    <div class="brand-name"><span class="brand-mark"></span>Hearth &amp; Basin Works</div>

    <ul class="contact-list">
      <li class="contact-item">
        <svg class="contact-icon" viewBox="0 0 24 24"><path d="M6.6 10.8a15.1 15.1 0 0 0 6.6 6.6l2.2-2.2a1 1 0 0 1 1-.25 11.4 11.4 0 0 0 3.6.57 1 1 0 0 1 1 1V20a1 1 0 0 1-1 1A17 17 0 0 1 3 4a1 1 0 0 1 1-1h3.5a1 1 0 0 1 1 1c0 1.250.2 2.45.57 3.57a1 1 0 0 1-.25 1z"/></svg>
        <span>515.284.7093</span>
      </li>
      <li class="contact-item">
        <svg class="contact-icon" viewBox="0 0 24 24"><path d="M2 5h20v14H2zm2 2v.5l8 5 8-5V7l-8 5z"/></svg>
        <span>hello@hbwplains.com</span>
      </li>
      <li class="contact-item">
        <svg class="contact-icon" viewBox="0 0 24 24"><path d="M12 2a7 7 0 0 0-7 7c0 5.2 7 13 7 13s7-7.8 7-13a7 7 0 0 0-7-7zm0 9.5A2.5 2.5 0 1 1 12 6.5a2.5 2.5 0 0 1 0 5z"/></svg>
        <span>218 NW Larkfield Rd. Suite 207<br>Ankeny, Iowa 50021</span>
      </li>
      <li class="contact-item">
        <svg class="contact-icon" viewBox="0 0 24 24"><path d="M12 2a10 10 0 1 0 0 20 10 10 0 0 0 0-20zm6.9 6h-3a15.6 15.6 0 0 0-1.4-3.6A8 8 0 0 1 18.9 8zM12 4c.8 1.2 1.5 2.5 1.9 4h-3.8c.4-1.5 1.1-2.8 1.9-4zM4.3 14a8 8 0 0 1 0-4h3.4a16 16 0 0 0 0 4zm.8 2h3a15.6 15.6 0 0 0 1.4 3.6A8 8 0 0 1 5.1 16zM8 8H5.1a8 8 0 0 1 4.4-3.6A15.6 15.6 0 0 0 8 8zm4 12c-.8-1.2-1.5-2.5-1.9-4h3.8c-.4 1.5-1.1 2.8-1.9 4zm2.3-6H9.7a14.6 14.6 0 0 1 0-4h4.6a14.6 14.6 0 0 1 0 4zm.2 5.6A15.6 15.6 0 0 0 16 16h2.9a8 8 0 0 1-4.4 3.6zm1.8-5.6a16 16 0 0 0 0-4h3.4a8 8 0 0 1 0 4z"/></svg>
        <span>hbwplains.com</span>
      </li>
    </ul>

    <div class="person">
      <p class="person-name"><span class="first">Your </span><span class="last">Namehere</span></p>
      <p class="person-title">DESIGNATION</p>
    </div>
  </section>

</main>
</body>
</html>
```